Industrial Professional Business Card Design (Vantrel KX)

Would like professional looking business cards. Not too busy leaning towards minimal. Should have a slogan like:
"Industrial Automation and Control".

We are a tech company that programs industrial PLC computers. We also develop custom hardware solutions. Please use the logo for inspiration.

Target Market(s)

Mining, industrial, processing, automation, factory

Industry/Entity Type

Engineering

Contact Information for Business Card

Name, phone, email, website. job title.

Font styles to use
Other font styles liked:
• droid sans

Requirements
Must have
• Use colours that go well with the logo. Not too busy design.

```html
<!DOCTYPE html>
<html lang="en">
<head>
<meta charset="utf-8">
<title>Vantrel KX Business Card</title>
<link rel="stylesheet" href="https://fonts.googleapis.com/css2?family=Montserrat:wght@500;600;700&family=Lato:wght@400;700&display=swap">
<style>
  :root {
    --navy: #1f3a66;
    --teal: #2b7399;
    --deep: #223a68;
    --orange: #e5672a;
    --white: #f7f7f7;
    --grey-text: #555a60;
    --backdrop: #e9e9ea;
  }
  * { box-sizing: border-box; margin: 0; padding: 0; }
  html, body { width: 1200px; height: 772px; overflow: hidden; }
  body {
    background: var(--backdrop);
    font-family: "Lato", sans-serif;
    position: relative;
  }
  .card {
    position: absolute;
    top: 231px;
    width: 540px;
    height: 309px;
    border-radius: 3px;
    overflow: hidden;
    box-shadow: 0 12px 30px rgba(0,0,0,0.16);
  }
  /* Back side */
  .card-back {
    left: 40px;
    background: linear-gradient(160deg, var(--teal) 0%, #285f8a 45%, var(--deep) 100%);
    display: flex;
    align-items: center;
    justify-content: center;
  }
  .brand {
    display: flex;
    align-items: center;
    gap: 14px;
  }
  .brand-dot {
    width: 46px; height: 46px;
    border-radius: 50%;
    background: var(--orange);
  }
  .brand-name {
    font-family: "Montserrat", sans-serif;
    font-weight: 500;
    font-size: 44px;
    letter-spacing: 0.5px;
    color: #3b79a6;
  }
  .card-back .brand-dot { background: #3b79a6; }
  /* Front side */
  .card-front {
    left: 620px;
    background: var(--white);
  }
  .front-body {
    position: absolute;
    inset: 0 0 52px 0;
    display: flex;
    align-items: center;
    padding: 0 30px 0 34px;
  }
  .front-body .brand-dot { width: 30px; height: 30px; }
  .front-body .brand-name { font-size: 28px; color: var(--navy); }
  .front-body .brand { gap: 10px; }
  .divider {
    width: 1.5px;
    height: 120px;
    background: var(--navy);
    margin: 0 22px;
  }
  .contact-name {
    font-family: "Montserrat", sans-serif;
    font-weight: 700;
    font-size: 17px;
    color: var(--navy);
    letter-spacing: 0.3px;
  }
  .contact-role {
    font-family: "Montserrat", sans-serif;
    font-weight: 600;
    font-size: 13px;
    color: var(--orange);
    margin: 2px 0 12px;
  }
  .contact-list { list-style: none; }
  .contact-list li {
    display: flex;
    align-items: center;
    gap: 7px;
    font-size: 12.5px;
    color: var(--grey-text);
    line-height: 20px;
  }
  .contact-list svg { width: 12px; height: 12px; flex: none; }
  .slogan-band {
    position: absolute;
    left: 0; right: 0; bottom: 0;
    height: 52px;
    background: linear-gradient(90deg, var(--teal), var(--deep));
    display: flex;
    align-items: center;
    justify-content: center;
    font-family: "Montserrat", sans-serif;
    font-weight: 500;
    font-size: 14px;
    letter-spacing: 3.2px;
    color: #ffffff;
  }
</style>
</head>
<body>
  <section class="card card-back">
    <div class="brand">
      <span class="brand-dot"></span>
      <span class="brand-name">Vantrel KX</span>
    </div>
  </section>

  <section class="card card-front">
    <div class="front-body">
      <div class="brand">
        <span class="brand-dot"></span>
        <span class="brand-name">Vantrel KX</span>
      </div>
      <div class="divider"></div>
      <div class="contact">
        <p class="contact-name">MAREK HOLLOWAY</p>
        <p class="contact-role">Director</p>
        <ul class="contact-list">
          <li>
            <svg viewBox="0 0 12 12"><path d="M2 1h2.5l1 3-1.5 1a6 6 0 0 0 3 3l1-1.5 3 1V10a1 1 0 0 1-1 1A9 9 0 0 1 1 2a1 1 0 0 1 1-1z" fill="#e5672a"/></svg>
            +49 30 555 018 247
          </li>
          <li>
            <svg viewBox="0 0 12 12"><rect x="0.5" y="2" width="11" height="8" fill="#e5672a"/><path d="M0.5 2 6 6.5 11.5 2" fill="none" stroke="#fff" stroke-width="1"/></svg>
            info@vantrelkx.com
          </li>
          <li>
            <svg viewBox="0 0 12 12"><circle cx="6" cy="6" r="5.5" fill="#e5672a"/><path d="M0.5 6h11M6 0.5c-2.5 3-2.5 8 0 11M6 0.5c2.5 3 2.5 8 0 11" fill="none" stroke="#fff" stroke-width="0.8"/></svg>
            www.vantrelkx.com
          </li>
        </ul>
      </div>
    </div>
    <div class="slogan-band">Industrial Automation and Control</div>
  </section>
</body>
</html>
```